Wine Label - Design required by La Brisuela

2 Independent chilean winemakers here!
La Brisuela (means door slam or slam), that is the brand for our wines (2 wines at the moment), low scale production.
We would like to have front label for our wine out of the mainstream typical french classic style. Some words to describe it: youthful yet vintage/ Tobiah Vance/ pellman/ comic/ old western. Something i would wear on a t-shirt.
The text that is has to be on the label:
- La Brisuela (the brand)
-Field Blend (the type of one of the wines we have)
- 2018
- Wine of Chile.
It goes on sloping shoulder bottle, Burgundy model.
It is meant to cover a space of 3 1/4 h x 4 1/2 w inches . (or 8,5 cm height x 11cm width).
We like colours so...be creative!
I have attached the "La Brisuela" logo. We can changed it of course.
Thanks !

Target Market(s)

young drinkers (legally allowed to drink!)

Font styles to use
Other font styles liked:
• stencil

Colors

Designer to choose colors to be used in the design.

Requirements
Should not have
• Obvious wine things like glasses of wine, vines, grapes etc.

```html
<!DOCTYPE html>
<html lang="en">
<head>
<meta charset="utf-8">
<title>La Brisuela – Field Blend 2018</title>
<link rel="stylesheet" href="https://fonts.googleapis.com/css2?family=Oswald:wght@500;700&display=swap">
<style>
  :root {
    --teal: #58a9a8;
    --teal-light: #62b3b2;
    --teal-dark: #4f9c9b;
    --cream: #ecdfc0;
    --navy: #1d2030;
    --red: #e13a40;
  }
  * { box-sizing: border-box; margin: 0; padding: 0; }
  html, body { width: 1200px; height: 927px; overflow: hidden; }
  body { background: var(--teal); }
  .label {
    position: relative;
    width: 1200px;
    height: 927px;
    background: radial-gradient(ellipse at 50% 45%, var(--teal-light) 0%, var(--teal) 60%, var(--teal-dark) 100%);
    overflow: hidden;
  }
  .ribbon { position: absolute; left: 0; top: 0; width: 1200px; height: 140px; }
  .origin {
    position: absolute; left: 0; right: 0; top: 36px;
    text-align: center;
    font-family: "Oswald", sans-serif; font-weight: 700;
    font-size: 66px; line-height: 76px; letter-spacing: 3px;
    color: var(--cream);
  }
  .makers {
    position: absolute; left: 0; right: 0; top: 146px;
    text-align: center;
    font-family: "Oswald", sans-serif; font-weight: 500;
    font-size: 25px; letter-spacing: 11px;
    color: var(--navy);
  }
  .burst {
    position: absolute; left: 258px; top: 184px;
    width: 756px; height: 540px;
    border-radius: 50%;
    background: radial-gradient(ellipse at 50% 50%, var(--red) 0%, var(--red) 30%, var(--navy) 52%, rgba(29,32,48,0.55) 66%, rgba(29,32,48,0) 72%);
  }
  .brand {
    position: absolute; left: 0; right: 0; top: 350px;
    text-align: center;
    font-family: "Oswald", sans-serif; font-weight: 700;
    font-size: 150px; line-height: 170px; letter-spacing: 4px;
    color: var(--cream);
  }
  .variety {
    position: absolute; left: 0; right: 0; top: 728px;
    text-align: center;
    font-family: "Oswald", sans-serif; font-weight: 700;
    font-size: 92px; line-height: 100px; letter-spacing: 2px;
    color: var(--cream);
  }
  .vintage {
    position: absolute; left: 350px; top: 838px;
    width: 498px; height: 74px;
    background: var(--navy);
    clip-path: polygon(4% 0, 96% 0, 100% 50%, 96% 100%, 4% 100%, 0 50%);
    text-align: center;
    font-family: "Oswald", sans-serif; font-weight: 700;
    font-size: 56px; line-height: 74px; letter-spacing: 14px;
    color: var(--cream);
  }
</style>
</head>
<body>
  <main class="label">
    <svg class="ribbon" viewBox="0 0 1200 140" aria-hidden="true">
      <polygon fill="#ecdfc0" points="221,40 340,40 340,108 221,108 248,74"/>
      <polygon fill="#ecdfc0" points="979,40 860,40 860,108 979,108 952,74"/>
    </svg>
    <p class="origin">WINE OF CHILE</p>
    <p class="makers">INDEPENDENT WINEMAKERS</p>

    <div class="burst" role="img" aria-label="Comic-style explosion burst in red and navy with halftone dots"></div>

    <h1 class="brand">LA BRISUELA</h1>

    <p class="variety">FIELD BLEND</p>
    <p class="vintage">2018</p>
  </main>
</body>
</html>
```